Lumen Botanicals Label Project- Updates made to project!

Project Scope: Branding opportunity for internet based skin care line. Design coordinating label for 4 different products. Each design shall be editable in Adobe Illustrator as a template including all fonts, symbols, and guides. Submit a design for all 4 products (preferably together as it would look on a retail shelf), business card, and logo.
Cleanser: STEP 1 Label Size: 5 x 4.5 inches (w x h) CALM CLEANSER
Toner: STEP 2 Label Size: 5 x 4.5 inches (w x h) TRANQUIL TONER- A piece of each crystal sits at the bottom of each solution. It coordinates with the "Quiet Heart" of our logo.
Serum STEP 3 Label Size: Label Size: 4.25 x 2.25 ANTI-AGING SERUM
Moisturizer: STEP 4 Label Size: Label Size: 1”x7.25” MOISTURIZER
Each label needs to include:
Front:
Attractive larger sized STEP #
Logo
Product name and short description
Decorative design Symbol(s)
Back:
Area on back to say short description
Directions for use
Larger area for ingredients
Website: www.lumenbotanicals-example.com
Address of distribution
Barcode

Lumen Skin Care, an esthetician created line provides organic and natural based products for all skin types. With an emphasis on anti-aging, this simple 4- step system can be used by many including pregnant and oncology consumers. The unique thing about our line is that the toners and serums contain crystals such as amethyst and rose quarts to promote Quiet Heart as well as outer beauty. Each product is handmade with natural, quality ingredients and are 70-90% Organic.
Target Market: Women ages 30-45 years old. This demographic is on the go, and wants a simple-easy to read label, & a skin care system that addresses her concerns. Just as this consumer is mindful of her fitness and what she puts in her body, she tends to purchase environmentally friendly, and natural products. Health and wellness trends reflect this, as organic beauty products are expected to grow 74% from 2013 to 2018. She enjoys meditation and yoga, and she is curious about eastern medicine holistic healing trends.

Company Name: Lumen Skin Care
Tagline: Quiet Heart- Bright Face
Package Feel: Simple, elegant easy to read step on each product. STEP 1: AM/PM. Attractive numbering. A symbol that reflects the brand. Not necessarily a Jewel or Crystal because the name speaks for itself. Beautiful, soft, eye catching design that draws the consumer to pick it up. Clear or white label welcomed. Some color palettes provided.
Descriptive words the packaging should represent: Yoga, Zen, mystic, eye catching, healing energy, natural, quality ingredients, sophisticated, beautiful, serenity, easy to read- bold-attractive numbering on front.
Inspiration Brands: VARLA Organics- Beautiful watercolor packaging that resonates a "feeling"

Attached are pictures of the packaging, inspirational pictures, skin care lines that are attractive, ect.

Packaging SPECS:

Cleanser:
Color Clear
Size 4 oz
Material PET
Case Pack
Neck Finish 24-410
Diameter 1.58 in / 4.013 cm
Height 6 in / 15.240 cm
Label Dimensions 5x4.5
Print Dimensions 5x4.5
Print Dimensions in (diameter)

TONER BOTTLE: Same as above

SERUM BOTTLE:
Color Clear
Size 2 oz
Material PET
Neck Finish 20-410
Diameter 1.358 in / 3.449 cm
Height 3.274 in / 8.316 cm

Moisturizer:
2.3 oz
Height:53 mm
Diameter: 60 mm
Neck: 58/400

Target Market(s)

Women ages 30-45 years old. This demographic is on the go, and wants a simple-easy to read label, & a skin care system that addresses her concerns. Just as this consumer is mindful of her fitness and what she puts in her body, she tends to purchase environmentally friendly, and natural products. Health and wellness trends reflect this, as organic beauty products are expected to grow 74% from 2013 to 2018. She enjoys meditation and yoga, and she is curious about eastern medicine holistic healing trends.

Industry/Entity Type

Skin Care Product

Contact Information for Business Card

Details given upon completion.

Logo Text

Lumen Botanicals Quiet Heart- Bright Face

Requirements
Must have
• A large step number on the front. Coordinating symbols and colors. Must have a professional retail look and be easy to read.
Nice to have
• Clean, simple, eye catching packaging. Watercolor designs. Designs that inspire "feelings" www.varlaorganics-example.com

```html
<!DOCTYPE html>
<html lang="en">
<head>
<meta charset="utf-8">
<title>Lumen Skin Care – Calm Cleanser Label</title>
<link href="https://fonts.googleapis.com/css2?family=Josefin+Sans:wght@300&family=Montserrat:wght@300&family=Crimson+Text&family=Playfair+Display:wght@400&display=swap" rel="stylesheet">
<style>
  :root {
    --page: #ffffff;
    --label: #f7f6f4;
    --ink: #1c1c1c;
    --muted-ink: #3a3a3a;
    --peach: #f4c7a6;
    --peach-light: #fae3d2;
    --blush: #f7ece6;
  }
  html, body {
    margin: 0;
    padding: 0;
    width: 799px;
    height: 1200px;
    overflow: hidden;
    background: var(--page);
  }
  .canvas {
    position: relative;
    width: 799px;
    height: 1200px;
  }
  .label {
    position: absolute;
    left: 180px;
    top: 100px;
    width: 440px;
    height: 1035px;
    background: var(--label);
    overflow: hidden;
    box-shadow: 0 0 0 1px #ecebe8;
  }
  .pattern-band {
    position: absolute;
    left: 0;
    width: 440px;
  }
  .pattern-band--top { top: 0; height: 360px; }
  .pattern-band--bottom { bottom: 0; height: 180px; }

  .brand {
    position: absolute;
    left: 68px;
    top: 248px;
    width: 360px;
    text-align: center;
    color: var(--ink);
    font-family: "Montserrat", sans-serif;
    font-weight: 300;
  }
  .brand__mark {
    display: block;
    width: 14px;
    height: 14px;
    margin: 0 auto 6px;
    border: 1px solid var(--ink);
    border-radius: 50%;
  }
  .brand__name {
    display: block;
    font-size: 40px;
    letter-spacing: 5px;
    line-height: 1;
  }
  .brand__sub {
    display: block;
    margin-top: 12px;
    font-size: 22px;
    letter-spacing: 5px;
    line-height: 1;
  }

  .tagline {
    position: absolute;
    left: 2px;
    top: 560px;
    transform: rotate(-90deg);
    transform-origin: left top;
    white-space: nowrap;
    font-family: "Montserrat", sans-serif;
    font-weight: 300;
    font-size: 23px;
    letter-spacing: 1.5px;
    color: var(--muted-ink);
    top: 890px;
  }

  .step-number {
    position: absolute;
    left: 40px;
    top: 520px;
    font-family: "Playfair Display", serif;
    font-size: 360px;
    line-height: 1;
    color: var(--ink);
  }

  .product-name {
    position: absolute;
    left: 172px;
    top: 708px;
    margin: 0;
    font-family: "Josefin Sans", sans-serif;
    font-weight: 300;
    font-size: 44px;
    line-height: 1.25;
    letter-spacing: 1px;
    color: var(--ink);
  }
  .product-name__rule {
    position: absolute;
    left: 172px;
    top: 810px;
    width: 242px;
    height: 0;
    border-top: 2px solid var(--ink);
  }
  .product-description {
    position: absolute;
    left: 63px;
    top: 820px;
    width: 370px;
    margin: 0;
    text-align: right;
    font-family: "Crimson Text", serif;
    font-size: 23px;
    color: var(--ink);
  }
</style>
</head>
<body>
<div class="canvas">
  <div class="label">
    <svg class="pattern-band pattern-band--top" viewBox="0 0 440 360" role="img" aria-label="Soft peach faceted crystal pattern band">
      <defs>
        <linearGradient id="peachTop" x1="0" y1="0" x2="1" y2="1">
          <stop offset="0" stop-color="#fae3d2"/>
          <stop offset="0.5" stop-color="#f4c7a6"/>
          <stop offset="1" stop-color="#f7ece6"/>
        </linearGradient>
      </defs>
      <path d="M0 0 H440 V300 C380 320 300 290 220 300 C140 312 70 350 0 340 Z" fill="url(#peachTop)"/>
    </svg>

    <svg class="pattern-band pattern-band--bottom" viewBox="0 0 440 180" role="img" aria-label="Soft peach faceted crystal pattern band">
      <defs>
        <linearGradient id="peachBottom" x1="0" y1="0" x2="1" y2="1">
          <stop offset="0" stop-color="#f7ece6"/>
          <stop offset="0.5" stop-color="#f4c7a6"/>
          <stop offset="1" stop-color="#fae3d2"/>
        </linearGradient>
      </defs>
      <path d="M0 30 C90 10 180 0 260 8 C330 14 390 4 440 0 V180 H0 Z" fill="url(#peachBottom)"/>
    </svg>

    <div class="brand">
      <span class="brand__mark"></span>
      <span class="brand__name">LUMEN</span>
      <span class="brand__sub">SKIN CARE</span>
    </div>

    <div class="tagline">quiet heart - bright face</div>

    <div class="step-number">1</div>

    <h1 class="product-name">CALM<br>CLEANSER</h1>
    <div class="product-name__rule"></div>
    <p class="product-description">product short description here</p>
  </div>
</div>
</body>
</html>
```